Social Media Graphics - ALL TEXT RK

We are looking for a series of social media graphics for Instagram (standard size 1:1 (1080x1080px) that are ALL TEXT. We want the following quotes below on each graphic; one quote per graphic. AND, In very small letters at the bottom of each graphic, add @RKMarlowLive

The look and feel of these graphics should be complimentary to the color palette attached below; but keep them simple. But the design is up to you; at the end of this document, I provided various samples of all text graphics that I like as examples.

Target Market(s)

women looking to lose weight

Industry/Entity Type

health and wellness

Colors
E54698
E96AAD
F1A4CE
F9D9EA
FCEFF6

Requirements
Must have
• the quotes in the document
Should not have
• no stock photography

```html
<!DOCTYPE html>
<html lang="en">
<head>
<meta charset="utf-8">
<title>RK Social Graphics – All Text Series</title>
<link href="https://fonts.googleapis.com/css2?family=Anton&family=Montserrat:wght@800&display=swap" rel="stylesheet">
<style>
  :root {
    --page: #ffffff;
    --maroon: #8a0042;
    --magenta: #ff0a8a;
    --pink: #e96aad;
    --blush: #f9d9ea;
    --glow: #fceff6;
    --ink-light: #ffffff;
    --ink-dark: #6e0033;
    --shadow: #5e002c;
  }
  html, body {
    margin: 0;
    width: 1200px;
    height: 1200px;
    overflow: hidden;
    background: var(--page);
  }
  .canvas {
    position: relative;
    width: 1200px;
    height: 1200px;
  }
  .tile {
    position: absolute;
    width: 503px;
    height: 502px;
    overflow: hidden;
  }
  .tile--bloating {
    left: 86px; top: 85px;
    background:
      radial-gradient(circle at 96% 60%, var(--ink-light) 0%, var(--blush) 14%, var(--pink) 38%, var(--magenta) 62%, transparent 95%),
      linear-gradient(135deg, var(--maroon) 0%, var(--magenta) 55%, var(--maroon) 100%);
  }
  .tile--fault,
  .tile--fault-bold {
    background:
      radial-gradient(ellipse 70% 45% at 50% 100%, var(--glow) 0%, var(--blush) 25%, var(--pink) 60%, transparent 100%),
      linear-gradient(180deg, var(--maroon) 0%, #c4005f 30%, var(--magenta) 58%, var(--pink) 100%);
  }
  .tile--fault { left: 610px; top: 85px; }
  .tile--fault-bold { left: 348px; top: 609px; }

  .quote-plain {
    position: absolute;
    left: 43px;
    top: 128px;
    margin: 0;
    font-family: "Montserrat", sans-serif;
    font-weight: 800;
    font-size: 33px;
    line-height: 35.5px;
    letter-spacing: -0.3px;
    color: var(--ink-light);
    text-transform: uppercase;
  }
  .handle {
    position: absolute;
    margin: 0;
    font-size: 18px;
    line-height: 1;
  }
  .tile--bloating .handle {
    left: 43px;
    top: 447px;
    font-family: "Montserrat", sans-serif;
    font-weight: 800;
    color: var(--ink-light);
  }
  .tile--fault .handle,
  .tile--fault-bold .handle {
    left: 0; right: 0;
    text-align: center;
    font-family: "Anton", sans-serif;
    font-size: 19px;
    color: var(--ink-dark);
  }
  .tile--fault .handle { top: 456px; }
  .tile--fault-bold .handle { top: 440px; }

  .quote-stack {
    position: absolute;
    left: 0; right: 0;
    top: 91px;
    margin: 0;
    text-align: center;
    font-family: "Anton", sans-serif;
    font-size: 54px;
    line-height: 58px;
    letter-spacing: -1.2px;
    color: var(--ink-light);
    text-shadow: 3px 3px 0 var(--shadow);
  }
  .quote-stack span { display: block; }

  .quote-scale {
    margin: 0;
    font-family: "Anton", sans-serif;
    color: var(--ink-light);
  }
  .quote-scale .line {
    position: absolute;
    left: 0; right: 0;
    text-align: center;
    line-height: 1;
    white-space: nowrap;
  }
  .line--small { font-size: 40px; letter-spacing: -0.8px; }
  .line--huge { font-size: 104px; letter-spacing: -2px; }
  .line--mid { font-size: 58px; letter-spacing: -1.2px; }
</style>
</head>
<body>
<main class="canvas">
  <section class="tile tile--bloating">
    <p class="quote-plain">Struggling with<br>bloating and<br>belly fat?<br>Try this natural<br>solution tonight,<br>and wake up<br>feeling lighter!</p>
    <p class="handle">@RKMarlowLive</p>
  </section>

  <section class="tile tile--fault">
    <p class="quote-stack">
      <span>THAT STUBBORN</span>
      <span>BELLY FAT</span>
      <span>ISN'T YOUR FAULT -</span>
      <span>HERE'S WHAT</span>
      <span>NO ONE TELLS YOU.</span>
    </p>
    <p class="handle">@RKMarlowLive</p>
  </section>

  <section class="tile tile--fault-bold">
    <p class="quote-scale">
      <span class="line line--small" style="top:40px">THAT STUBBORN</span>
      <span class="line line--small" style="top:80px">BELLY FAT</span>
      <span class="line line--huge" style="top:122px">ISN'T YOUR</span>
      <span class="line line--huge" style="top:212px">FAULT</span>
      <span class="line line--small" style="top:313px">HERE'S WHAT</span>
      <span class="line line--mid" style="top:357px">NO ONE TELLS YOU.</span>
    </p>
    <p class="handle">@RKMarlowLive</p>
  </section>
</main>
</body>
</html>
```